Menu redesign of existing iPhone app Lumora

We need a design upgrade for a footer menu of an iPhone app. We need to incorporate a new button for competitions/missions and it should be extremely modern and clean. The central button to create a Lumora cannot be too different as our current users are familiar with its usage.

I have attached screenshots of the curent newsfeed and menu.

Target Market(s)

Photography lovers/ design lovers

Font styles to use
Sans Serif

Requirements
Must have
• Lumora Button,
• Home button,
• My Profile button,
• Find friends button,
• Notifications button,
• Settings button,
• Missions/Competition Button
Nice to have
• Similar Lumora button as existing on the app

```html
<!DOCTYPE html>
<html lang="en">
<head>
<meta charset="utf-8">
<title>Lumora – Newsfeed with footer menu</title>
<link href="https://fonts.googleapis.com/css2?family=Open+Sans:ital,wght@0,400;0,600;1,400;1,600&display=swap" rel="stylesheet">
<style>
  :root {
    --page-bg: #ececec;
    --screen-bg: #ffffff;
    --ink: #1d1d1f;
    --ink-soft: #555a60;
    --accent: #3d9be9;
    --accent-dark: #2a86d6;
    --rule: #e3e3e3;
    --footer-bg: rgba(255,255,255,0.94);
  }
  * { box-sizing: border-box; margin: 0; padding: 0; }
  html, body {
    width: 1052px; height: 1200px; overflow: hidden;
    background: var(--page-bg);
    font-family: "Open Sans", "Helvetica Neue", Arial, sans-serif;
    color: var(--ink);
  }
  .screen {
    position: absolute; left: 226px; top: 66px;
    width: 600px; height: 1067px;
    background: var(--screen-bg);
    overflow: hidden;
    box-shadow: 0 20px 60px rgba(0,0,0,0.12);
    display: flex; flex-direction: column;
  }
  .status-bar {
    height: 34px; flex: none;
    display: flex; align-items: center; justify-content: space-between;
    padding: 0 14px;
    font-size: 18px; font-style: italic; color: var(--ink-soft);
  }
  .status-left { display: flex; align-items: center; gap: 8px; }
  .signal { display: flex; gap: 3px; }
  .signal i { width: 8px; height: 8px; border-radius: 50%; background: var(--ink-soft); }
  .signal i.off { background: none; border: 1px solid var(--ink-soft); }
  .status-right { display: flex; align-items: center; gap: 8px; }
  .battery { width: 38px; height: 16px; border: 1.5px solid var(--ink-soft); border-radius: 3px; padding: 2px; }
  .battery span { display: block; height: 100%; background: var(--ink-soft); border-radius: 1px; }

  .post-header {
    height: 90px; flex: none;
    display: flex; align-items: center;
    padding: 0 18px 0 12px;
    border-bottom: 1px solid var(--rule);
  }
  .avatar {
    width: 62px; height: 62px; border-radius: 50%;
    background: radial-gradient(circle at 50% 40%, #e9e4de, #8b7f74 70%, #4b433d);
    flex: none;
  }
  .post-meta { margin-left: 16px; flex: 1; }
  .post-author { font-size: 20px; font-weight: 600; line-height: 1.2; }
  .post-time { display: flex; align-items: center; gap: 6px; font-size: 14px; font-style: italic; color: var(--ink-soft); margin-top: 4px; }
  .post-stats { display: flex; gap: 26px; align-self: flex-end; margin-bottom: 16px; font-size: 17px; font-style: italic; }
  .stat { display: flex; align-items: center; gap: 6px; }

  .post-photo {
    flex: 1;
    background:
      linear-gradient(180deg,
        #a9cbe6 0%, #d6e7f3 22%, #f4f8fb 45%, #f1f3ea 60%,
        #8fb06a 72%, #6b8a45 80%, #a58763 88%, #7d6248 100%);
  }

  .footer-menu {
    height: 100px; flex: none;
    background: var(--footer-bg);
    display: flex; align-items: center; justify-content: space-between;
    padding: 0 30px;
    border-top: 1px solid var(--rule);
  }
  .menu-button { width: 40px; height: 40px; display: flex; align-items: center; justify-content: center; }
  .create-button {
    width: 62px; height: 62px; border-radius: 50%;
    background: var(--accent);
    display: flex; align-items: center; justify-content: center;
    box-shadow: 0 2px 6px rgba(42,134,214,0.35);
  }
  .create-button span { width: 20px; height: 20px; border-radius: 50%; background: #fff; }
  .menu-icon { fill: none; stroke: var(--accent); stroke-width: 2; stroke-linecap: round; stroke-linejoin: round; }
</style>
</head>
<body>
  <main class="screen">
    <div class="status-bar">
      <div class="status-left">
        <div class="signal"><i></i><i></i><i></i><i></i><i class="off"></i></div>
        <span class="carrier">Corvel</span>
        <svg width="20" height="15" viewBox="0 0 20 15" aria-hidden="true"><path d="M1 5a13 13 0 0 1 18 0M4 8.5a8 8 0 0 1 12 0M7 11.5a3.5 3.5 0 0 1 6 0" fill="none" stroke="#555a60" stroke-width="1.8" stroke-linecap="round"/></svg>
      </div>
      <span class="clock">12:02 AM</span>
      <div class="status-right">
        <span>100%</span>
        <div class="battery"><span></span></div>
      </div>
    </div>

    <header class="post-header">
      <div class="avatar" role="img" aria-label="Profile photo of the poster"></div>
      <div class="post-meta">
        <div class="post-author">Harbor Foxes</div>
        <div class="post-time">
          <svg width="14" height="14" viewBox="0 0 14 14" aria-hidden="true"><circle cx="7" cy="7.5" r="5.3" fill="none" stroke="#3d9be9" stroke-width="1.6"/><path d="M7 5v2.8l1.8 1.2" fill="none" stroke="#3d9be9" stroke-width="1.4" stroke-linecap="round"/></svg>
          43 minutes ago
        </div>
      </div>
      <div class="post-stats">
        <div class="stat">
          <svg width="18" height="16" viewBox="0 0 18 16" aria-hidden="true"><path d="M9 15S1 10 1 5a4 4 0 0 1 8-1 4 4 0 0 1 8 1c0 5-8 10-8 10z" fill="#3d9be9"/></svg>
          09
        </div>
        <div class="stat">
          <svg width="18" height="17" viewBox="0 0 18 17" aria-hidden="true"><path d="M9 1a8 7 0 1 1-4 13L1 16l1.5-3.5A8 7 0 0 1 9 1z" fill="#3d9be9"/></svg>
          13
        </div>
      </div>
    </header>

    <div class="post-photo" role="img" aria-label="Photo of a runner on a sunlit dirt trail with grass and sky"></div>

    <nav class="footer-menu" aria-label="Main menu">
      <a class="menu-button home-button" aria-label="Home">
        <svg width="36" height="34" viewBox="0 0 38 36" aria-hidden="true"><path class="menu-icon" d="M3 17L19 3l16 14M7 14v19h9v-10h6v10h9V14"/></svg>
      </a>
      <a class="menu-button friends-button" aria-label="Find friends">
        <svg width="34" height="34" viewBox="0 0 34 34" aria-hidden="true"><circle class="menu-icon" cx="13" cy="12" r="6"/><path class="menu-icon" d="M2 30c0-6 5-10 11-10s11 4 11 10"/><path class="menu-icon" d="M28 9v10M23 14h10"/></svg>
      </a>
      <a class="menu-button profile-button" aria-label="My profile">
        <svg width="32" height="34" viewBox="0 0 32 34" aria-hidden="true"><circle class="menu-icon" cx="16" cy="11" r="7"/><path class="menu-icon" d="M3 31c0-7 6-11 13-11s13 4 13 11"/></svg>
      </a>
      <a class="create-button" aria-label="Create a Lumora"><span></span></a>
      <a class="menu-button notifications-button" aria-label="Notifications">
        <svg width="32" height="34" viewBox="0 0 32 34" aria-hidden="true"><path class="menu-icon" d="M6 25V15a10 10 0 0 1 20 0v10l3 3H3z"/><path class="menu-icon" d="M13 31a3 3 0 0 0 6 0"/></svg>
      </a>
      <a class="menu-button settings-button" aria-label="Settings">
        <svg width="34" height="34" viewBox="0 0 34 34" aria-hidden="true"><circle class="menu-icon" cx="17" cy="17" r="5"/><path class="menu-icon" d="M17 3v5M17 26v5M3 17h5M26 17h5M7 7l3.5 3.5M23.5 23.5L27 27M27 7l-3.5 3.5M10.5 23.5L7 27"/></svg>
      </a>
      <a class="menu-button missions-button" aria-label="Missions and competitions">
        <svg width="30" height="34" viewBox="0 0 30 34" aria-hidden="true"><path class="menu-icon" d="M6 32L26 3M13 3h13v13"/></svg>
      </a>
    </nav>
  </main>
</body>
</html>
```